Re-launching marine insurance adjusting company - looking for energy

I am a sole practitioner specializing in the profession of average adjusting. There is an on-line brochure at www.rkbtnova.com I am one of only a handful of specialists in this field and I enjoy a fair amount of name recognition, domestically in the US and internationally. My principal markets are the US, the London and Scandinavian insurance markets and shipowners and insurers in Latin America.
The business is a mixture of law, accounting and insurance and my clientele relies on a time-sensitive and accurate work-product, clearly stating an insurance company's liability for a given claim. The identity needs to project gravitas rather than flash.
Since 1998 I have traded as "The Halloway Company" but have also attempted to establish the name RKBNOVA.com so that people would visit my website.
I want to implement a single identity across my stationery, business cards and website. I have come to see "The Halloway Company" as rather fatuous, since there is no company, it is just me. The Internet domain RKBNOVA is long-established and I would be reluctant to change it. I have considered trading as simply Marcus T Halloway, MTH, RKBNOVA or attempting to come up with a name that could be abbreviated to MTH, e.g. M Halloway Trelantics - but I can't find a suitable word for the second S.
Logo-wise, I have considered a stylized MTH or RKBNOVA redolent of waves of the sea. A nautical theme embodying a cargo ship, navigational beacon or lighthouse might be appropriate but these tend to be hackneyed.
I have attached a card that I mocked up at Pix, connoting stacking up numbers, which I really like, but I think it is too cryptic for people in most insurance companies, who don't particularly think laterally or they wouldn't work in marine insurance, and the card that I use currently, which I intended to be understated, but in fact it states nothing.
I have also attached my current letterhead, to demonstrate how I really need help.
Finally, I have attached a credentials sheet, to attempt to establish how narrow and deep is the professional niche that I occupy.
What I am looking to implement is a single logo, font, them and color scheme to use across my website, letterhead and business cards.
Over to the Sketch Guild...
Target Market(s)
Ship owners and insurance companies
Industry/Entity Type
Accounting

```html
<!DOCTYPE html>
<html lang="en">
<head>
<meta charset="utf-8">
<title>RKBNOVA Letterhead</title>
<link href="https://fonts.googleapis.com/css2?family=Open+Sans:wght@400;600;700&display=swap" rel="stylesheet">
<style>
  :root {
    --backdrop: #939498;
    --paper: #ffffff;
    --brand-blue: #0d4a9c;
    --sea-light: #2a88cf;
    --sea-deep: #0b4497;
    --ink: #3a3a3a;
    --rule: #9aa3ad;
  }
  html, body {
    margin: 0;
    padding: 0;
    width: 1200px;
    height: 1000px;
    overflow: hidden;
    background: var(--backdrop);
    font-family: "Open Sans", Arial, sans-serif;
  }
  .letterhead {
    position: absolute;
    left: 280px;
    top: 86px;
    width: 640px;
    height: 828px;
    background: var(--paper);
    overflow: hidden;
  }
  .brand {
    position: absolute;
    left: 92px;
    top: 62px;
    display: flex;
    align-items: center;
    gap: 12px;
  }
  .brand-dot {
    width: 20px;
    height: 20px;
    border-radius: 50%;
    background: var(--brand-blue);
  }
  .brand-name {
    font-weight: 600;
    font-size: 32px;
    line-height: 1;
    color: var(--brand-blue);
    letter-spacing: 0.3px;
  }
  .contact {
    position: absolute;
    right: 36px;
    top: 48px;
    display: flex;
    align-items: flex-start;
    gap: 8px;
  }
  .contact-address {
    margin-top: 18px;
    text-align: right;
    font-style: normal;
    font-size: 8px;
    line-height: 10px;
    color: var(--ink);
  }
  .contact-divider {
    width: 1px;
    height: 56px;
    background: var(--rule);
  }
  .contact-list {
    list-style: none;
    margin: 0;
    padding: 0;
    font-size: 8.5px;
    line-height: 14px;
    color: var(--ink);
  }
  .contact-list li {
    display: flex;
    align-items: center;
    gap: 6px;
  }
  .contact-icon {
    width: 10px;
    height: 10px;
    flex: none;
  }
  .sea-footer {
    position: absolute;
    left: 0;
    bottom: 0;
    width: 640px;
    height: 90px;
    background: linear-gradient(180deg, var(--sea-light) 0%, var(--sea-deep) 100%);
  }
</style>
</head>
<body>
  <main class="letterhead">
    <header>
      <div class="brand">
        <span class="brand-dot"></span>
        <span class="brand-name">RKBNOVA</span>
      </div>
      <div class="contact">
        <address class="contact-address">
          48 Harbor View Lane<br>Bayport, NY 11705, USA
        </address>
        <span class="contact-divider"></span>
        <ul class="contact-list">
          <li>
            <svg class="contact-icon" viewBox="0 0 10 10"><circle cx="5" cy="5" r="5" fill="var(--brand-blue)"/><path d="M3 2.6c.4-.3.8-.2 1 .2l.3.7c.1.3 0 .5-.2.7l-.3.2c.3.7.8 1.2 1.5 1.5l.2-.3c.2-.2.4-.3.7-.2l.7.3c.4.2.5.6.2 1-.5.6-1.2.7-2 .3C4 6.4 3.4 5.8 3 5c-.4-.8-.4-1.7 0-2.4z" fill="#fff"/></svg>
            (555) 318 2046
          </li>
          <li>
            <svg class="contact-icon" viewBox="0 0 10 10"><circle cx="5" cy="5" r="5" fill="var(--brand-blue)"/><rect x="3.4" y="2.2" width="3.2" height="5.6" rx=".6" fill="#fff"/><rect x="3.9" y="2.9" width="2.2" height="3.6" fill="var(--brand-blue)"/></svg>
            (555) 274 9013
          </li>
          <li>
            <svg class="contact-icon" viewBox="0 0 10 10"><circle cx="5" cy="5" r="5" fill="var(--brand-blue)"/><rect x="2.4" y="3.2" width="5.2" height="3.6" rx=".4" fill="#fff"/><path d="M2.6 3.4 5 5.2 7.4 3.4" stroke="var(--brand-blue)" stroke-width=".6" fill="none"/></svg>
            info@rkbnova.com
          </li>
          <li>
            <svg class="contact-icon" viewBox="0 0 10 10"><circle cx="5" cy="5" r="5" fill="var(--brand-blue)"/><circle cx="5" cy="5" r="2.7" fill="none" stroke="#fff" stroke-width=".7"/><path d="M2.3 5h5.4M5 2.3c-1.2 1.5-1.2 3.9 0 5.4M5 2.3c1.2 1.5 1.2 3.9 0 5.4" stroke="#fff" stroke-width=".6" fill="none"/></svg>
            www.rkbnova.com
          </li>
        </ul>
      </div>
    </header>

    <div class="sea-footer" role="img" aria-label="Decorative sea wave band in light and deep blue"></div>
  </main>
</body>
</html>
```